Online store website

Online store dealing on hoodies, joggers, trainers, baseball caps, trucker caps, winter hats, waist bands, jewelry sports and yoga suits , all women and men accessories.
All are my brand name Kelvo-trabrand.
I have a domain already

```html
<!DOCTYPE html>
<html lang="en">
<head>
<meta charset="utf-8">
<title>Kelvo-trabrand — Online Store</title>
<link href="https://fonts.googleapis.com/css2?family=Poppins:wght@400;500;600;700&display=swap" rel="stylesheet">
<style>
:root{
  --navy:#0d2a78;
  --navy-deep:#0a2366;
  --yellow:#f7b50c;
  --yellow-soft:#f9c53a;
  --ice:#e3ebf4;
  --ink:#1a1a2e;
  --muted:#5b5f6e;
  --white:#ffffff;
}
*{box-sizing:border-box;margin:0;padding:0}
html,body{width:1200px;height:4301px;overflow:hidden}
body{position:relative;font-family:"Poppins",sans-serif;color:var(--ink);background:var(--white)}
.abs{position:absolute}
a{color:inherit;text-decoration:none}

/* top bar */
.topbar{left:0;top:0;width:1200px;height:47px;background:var(--navy);color:var(--white);font-size:15px;font-weight:500}
.topbar .contact{left:110px;top:13px;display:flex;gap:22px;align-items:center}
.topbar .tools{right:110px;top:13px;display:flex;gap:16px;align-items:center;font-weight:600;font-size:14px}
.ico{display:inline-block;width:14px;height:14px;vertical-align:-2px;margin-right:6px}

/* header */
.header{left:0;top:47px;width:1200px;height:98px;background:var(--white)}
.brand{font-weight:500;font-size:27px;color:var(--navy);letter-spacing:-.3px}
.header .brand{left:110px;top:30px}
.nav{left:420px;top:37px;display:flex;align-items:center;gap:22px;font-size:13.5px;font-weight:600;text-transform:uppercase;color:var(--ink)}
.nav .active{background:var(--navy);color:var(--white);padding:7px 20px;border-radius:20px}
.cart{left:975px;top:30px;display:flex;align-items:center;gap:14px}
.cart .bubble{width:46px;height:46px;border-radius:50%;background:var(--white);box-shadow:0 6px 16px rgba(13,42,120,.18);display:flex;align-items:center;justify-content:center}
.cart small{display:block;font-size:12px;font-weight:600}
.cart strong{display:block;font-size:21px;color:var(--yellow);font-weight:600;line-height:1}

/* hero */
.hero{left:0;top:145px;width:1200px;height:640px;background:linear-gradient(90deg,#e9e9e9 0%,#f1f1f1 45%,#ececec 100%)}
.hero-photo{left:560px;top:0;width:640px;height:600px;background:radial-gradient(ellipse at 45% 40%,#f07a24 0%,#e9672a 22%,#e7e2dc 55%,#eeeeee 80%)}
.eyebrow{font-size:19px;font-weight:500;color:var(--yellow)}
.hero .eyebrow{left:112px;top:152px}
.hero h1{left:110px;top:180px;font-size:41px;font-weight:600;color:var(--navy);letter-spacing:-.5px}
.hero p{left:112px;top:238px;width:520px;font-size:19px;line-height:28px;color:var(--ink)}
.btn{display:inline-flex;align-items:center;justify-content:center;background:var(--navy);color:var(--white);font-weight:600;font-size:15px;text-transform:uppercase;border-radius:26px}
.hero .btn{left:112px;top:316px;width:142px;height:46px}
.dots{left:1139px;top:214px;display:flex;flex-direction:column;gap:10px}
.dots span{width:15px;height:15px;border-radius:50%;border:1.5px solid #8a8fa0}
.dots span.on{background:var(--navy);border-color:var(--navy)}
.hero-wave{left:0;top:560px}

/* section titles */
.title{width:1200px;left:0;text-align:center;font-size:45px;font-weight:600;color:var(--navy);letter-spacing:-.8px}
.title::after{content:"";display:block;width:74px;height:4px;background:var(--yellow);margin:6px auto 0;border-radius:2px}

/* arrows */
.arrow{width:40px;height:24px}

/* category */
.cat{width:305px;height:288px;background:var(--white);border-radius:14px;box-shadow:0 10px 28px rgba(13,42,120,.12)}
.cat .photo{left:17px;top:17px;width:271px;height:197px;border-radius:14px}
.cat h3{left:0;width:100%;top:235px;text-align:center;font-size:20px;font-weight:600;color:var(--navy)}
.cat.active{background:var(--navy)}
.cat.active h3{color:var(--yellow)}

/* products */
.band-ice{left:0;width:1200px;background:var(--ice)}
.prod{width:225px;height:316px;background:var(--white);border-radius:16px;box-shadow:0 10px 24px rgba(13,42,120,.14)}
.prod.active{border:3px solid var(--navy)}
.prod .photo{left:42px;top:22px;width:140px;height:145px;border-radius:10px}
.prod .add{right:14px;top:12px;width:30px;height:30px;border-radius:50%;border:1.5px solid var(--yellow);background:var(--white);display:flex;align-items:center;justify-content:center}
.prod.active .add{background:var(--yellow)}
.stars{color:var(--yellow);font-size:12px;letter-spacing:2px}
.prod .stars{left:0;width:100%;top:184px;text-align:center}
.prod h4{left:0;width:100%;top:207px;text-align:center;font-size:17px;font-weight:500;line-height:25px}
.prod .price{left:0;width:100%;top:262px;text-align:center;font-size:17px;font-weight:600}
.prod-btn{width:140px;height:42px}

/* history */
.history{left:0;top:1931px;width:1200px;height:614px;background:linear-gradient(120deg,#f0ad06 0%,#f7b80f 45%,#f6b60e 70%,#f3b20a 100%)}
.ring{left:110px;top:63px;width:488px;height:488px;border-radius:50%;background:var(--navy)}
.ring .photo{left:22px;top:22px;width:444px;height:444px;border-radius:50%;background:radial-gradient(circle at 60% 55%,#2f7b8d 0%,#3e8ea0 25%,#caa27a 55%,#d9c3a6 80%)}
.history h2{left:649px;top:92px;font-size:45px;font-weight:600;color:var(--navy);letter-spacing:-.8px}
.history h2::after{content:"";display:block;width:74px;height:4px;background:var(--navy);margin-top:4px}
.history p{left:649px;width:440px;font-size:15.5px;line-height:25px;color:var(--navy);text-align:justify}
.history .btn{left:649px;top:460px;width:142px;height:46px}

/* testimonials */
.quote{width:305px;height:288px;background:var(--white);border-top:4px solid var(--navy);border-radius:10px;box-shadow:0 10px 24px rgba(13,42,120,.1)}
.avatar{width:94px;height:94px;border-radius:50%;border:4px solid var(--navy);background:radial-gradient(circle,#c9a58a 0%,#9b7a64 60%,#e7e2dc 100%)}
.quote h5{left:0;width:100%;top:72px;text-align:center;font-size:17px;font-weight:600;color:var(--navy)}
.quote .stars{left:0;width:100%;top:98px;text-align:center}
.quote p{left:22px;width:261px;top:122px;text-align:center;font-size:14.5px;line-height:25px;color:var(--ink)}
.pager{width:36px;height:36px;border-radius:50%;display:flex;align-items:center;justify-content:center}

/* footer */
.footer{left:0;top:3972px;width:1200px;height:329px;background:var(--navy);color:var(--white)}
.footer .brand{left:110px;top:140px;color:var(--white)}
.footer h6{font-size:17px;font-weight:600;text-transform:uppercase}
.links{list-style:none;font-size:15px}
.links li{position:relative;height:40px;padding-left:26px}
.links li::before{content:"";position:absolute;left:0;top:9px;width:6px;height:6px;border-radius:50%;background:var(--yellow)}
.info{display:flex;align-items:flex-start;gap:16px;font-size:15px;line-height:22px}
.info .badge{width:36px;height:36px;flex:none;border-radius:50%;background:var(--white);display:flex;align-items:center;justify-content:center}
.rule{left:110px;top:240px;width:980px;height:1px;background:rgba(255,255,255,.15)}
.cards{left:112px;top:288px;display:flex;gap:5px}
.cards span{width:32px;height:19px;border-radius:3px;background:var(--white)}
.copyright{left:0;width:1200px;top:287px;text-align:center;font-size:12.5px;font-weight:500;text-transform:uppercase}
.social{left:922px;top:278px;display:flex;gap:8px}
.social span{width:36px;height:36px;border-radius:50%;border:1.5px solid var(--white)}
.social span.on{background:var(--yellow);border-color:var(--yellow)}
</style>
</head>
<body>

<!-- top bar -->
<div class="abs topbar">
  <div class="abs contact">
    <span><svg class="ico" viewBox="0 0 16 16" fill="#f7b50c"><path d="M3 1l3 3-2 2c1 2 3 4 5 5l2-2 3 3-2 3C7 14 2 9 1 3z"/></svg>+1 (555) 014 2290</span>
    <span>|</span>
    <span><svg class="ico" viewBox="0 0 16 16" fill="#f7b50c"><rect x="1" y="3" width="14" height="10" rx="1"/><path d="M1 4l7 5 7-5" stroke="#0d2a78" fill="none" stroke-width="1.4"/></svg>info@kelvo-trabrand.com</span>
  </div>
  <div class="abs tools">
    <svg width="15" height="15" viewBox="0 0 16 16" fill="none" stroke="#fff" stroke-width="2"><circle cx="7" cy="7" r="5"/><path d="M11 11l4 4"/></svg>
    <span>|</span>
    <span><svg class="ico" viewBox="0 0 16 16" fill="#fff"><circle cx="8" cy="5" r="3.5"/><path d="M1 15c0-4 3-6 7-6s7 2 7 6z"/></svg>LOGIN</span>
  </div>
</div>

<!-- header -->
<header class="abs header">
  <div class="abs brand">Kelvo-trabrand</div>
  <nav class="abs nav">
    <a class="active">Home</a><a>Shop by Category</a><a>Deals</a><a>About Us</a><a>Contact</a>
  </nav>
  <div class="abs cart">
    <div class="bubble"><svg width="18" height="16" viewBox="0 0 18 16" fill="#0d2a78"><path d="M0 1h3l1 2h13l-2 7H5L3 2H0z"/><circle cx="6" cy="13.5" r="1.6"/><circle cx="14" cy="13.5" r="1.6"/></svg></div>
    <div><small>CART:</small><strong>$0.00</strong></div>
  </div>
</header>

<!-- hero -->
<section class="abs hero">
  <div class="abs hero-photo" role="img" aria-label="Model in an orange hoodie and white joggers seated on a stool"></div>
  <div class="abs eyebrow">Kelvo-trabrand</div>
  <h1 class="abs">ELEVATE YOUR STYLE</h1>
  <p class="abs">Lorem ipsum dolor sit amet, consectetur adipiscing eiusmod tempor incididuntea.</p>
  <a class="abs btn">Shop Now</a>
  <div class="abs dots"><span></span><span class="on"></span><span></span><span></span></div>
</section>
<svg class="abs hero-wave" width="1200" height="240" viewBox="0 0 1200 240">
  <path d="M0 200 C260 70 480 235 780 232 C1000 228 1120 110 1200 55 L1200 240 L0 240Z" fill="#f7b50c"/>
  <path d="M0 218 C280 110 500 250 790 248 C1010 246 1130 130 1200 82 L1200 240 L0 240Z" fill="#fff"/>
</svg>

<!-- shop by category -->
<h2 class="abs title" style="top:848px">SHOP BY CATEGORY</h2>
<svg class="abs arrow" style="left:37px;top:1093px" viewBox="0 0 40 24" fill="none" stroke="#555" stroke-width="2.2"><path d="M39 12H2M12 2L2 12l10 10"/></svg>
<svg class="abs arrow" style="left:1123px;top:1093px" viewBox="0 0 40 24" fill="none" stroke="#555" stroke-width="2.2"><path d="M1 12h37M28 2l10 10-10 10"/></svg>

<div class="abs cat" style="left:112px;top:960px">
  <div class="abs photo" role="img" aria-label="Couple in hoodies on a beach" style="background:linear-gradient(160deg,#b9c3cc 0%,#8b9aa3 40%,#6b2a30 75%,#c9b8a3 100%)"></div>
  <h3 class="abs">HOODIES</h3>
</div>
<div class="abs cat active" style="left:447px;top:960px">
  <div class="abs photo" role="img" aria-label="Woman wearing gold jewelry" style="background:radial-gradient(circle at 50% 45%,#e8c2a4 0%,#d7a889 40%,#f0dccd 100%)"></div>
  <h3 class="abs">JEWELRY</h3>
</div>
<div class="abs cat" style="left:783px;top:960px">
  <div class="abs photo" role="img" aria-label="Two people jogging along a waterfront" style="background:linear-gradient(180deg,#e3b8a8 0%,#9a8d8f 45%,#4c5663 75%,#a07c6a 100%)"></div>
  <h3 class="abs">JOGGERS</h3>
</div>

<!-- featured products -->
<div class="abs band-ice" style="top:1349px;height:582px"></div>
<h2 class="abs title" style="top:1405px">FEATURED PRODUCTS</h2>
<svg class="abs arrow" style="left:37px;top:1675px" viewBox="0 0 40 24" fill="none" stroke="#555" stroke-width="2.2"><path d="M39 12H2M12 2L2 12l10 10"/></svg>
<svg class="abs arrow" style="left:1123px;top:1675px" viewBox="0 0 40 24" fill="none" stroke="#555" stroke-width="2.2"><path d="M1 12h37M28 2l10 10-10 10"/></svg>

<div class="abs prod" style="left:112px;top:1517px">
  <div class="abs add"><svg width="13" height="12" viewBox="0 0 18 16" fill="#f7b50c"><path d="M0 1h3l1 2h13l-2 7H5L3 2H0z"/><circle cx="6" cy="13.5" r="1.8"/><circle cx="14" cy="13.5" r="1.8"/></svg></div>
  <div class="abs photo" role="img" aria-label="Black hoodie" style="background:radial-gradient(circle,#2a2a2a 0%,#3a3a3a 50%,#f4f4f4 75%)"></div>
  <div class="abs stars">★★★★★</div>
  <h4 class="abs">Lorem ipsum dolor sit<br>amet consea</h4>
  <div class="abs price">$40.00</div>
</div>
<div class="abs prod" style="left:362px;top:1517px">
  <div class="abs add"><svg width="13" height="12" viewBox="0 0 18 16" fill="#f7b50c"><path d="M0 1h3l1 2h13l-2 7H5L3 2H0z"/><circle cx="6" cy="13.5" r="1.8"/><circle cx="14" cy="13.5" r="1.8"/></svg></div>
  <div class="abs photo" role="img" aria-label="Navy trucker cap" style="background:radial-gradient(ellipse,#1e2a44 0%,#2c3a5c 45%,#f4f4f4 75%)"></div>
  <div class="abs stars">★★★★★</div>
  <h4 class="abs">Lorem ipsum dolor sit<br>amet consea</h4>
  <div class="abs price">$65.00</div>
</div>
<div class="abs prod active" style="left:612px;top:1515px;width:226px;height:320px">
  <div class="abs add"><svg width="13" height="12" viewBox="0 0 18 16" fill="#0d2a78"><path d="M0 1h3l1 2h13l-2 7H5L3 2H0z"/><circle cx="6" cy="13.5" r="1.8"/><circle cx="14" cy="13.5" r="1.8"/></svg></div>
  <div class="abs photo" role="img" aria-label="Rolled blue yoga mat" style="background:radial-gradient(ellipse,#4c5fd6 0%,#5a6ce0 45%,#f4f4f4 75%)"></div>
  <div class="abs stars">★★★★★</div>
  <h4 class="abs">Lorem ipsum dolor sit<br>amet consea</h4>
  <div class="abs price">$40.00</div>
</div>
<a class="abs btn prod-btn" style="left:655px;top:1813px">Shop Now</a>
<div class="abs prod" style="left:863px;top:1517px">
  <div class="abs add"><svg width="13" height="12" viewBox="0 0 18 16" fill="#f7b50c"><path d="M0 1h3l1 2h13l-2 7H5L3 2H0z"/><circle cx="6" cy="13.5" r="1.8"/><circle cx="14" cy="13.5" r="1.8"/></svg></div>
  <div class="abs photo" role="img" aria-label="Silver diamond ring" style="background:radial-gradient(circle,#c9ccd2 0%,#e1e3e7 45%,#f6f6f6 75%)"></div>
  <div class="abs stars">★★★★★</div>
  <h4 class="abs">Lorem ipsum dolor sit<br>amet consea</h4>
  <div class="abs price">$65.00</div>
</div>

<!-- our history -->
<section class="abs history">
  <div class="abs ring"><div class="abs photo" role="img" aria-label="Hands rolling up a teal yoga mat on a wooden floor"></div></div>
  <h2 class="abs">OUR HISTORY</h2>
  <p class="abs" style="top:195px">Lorem ipsum dolor sit amet, consectetur adipiscing elit, sed do eiusmod tempor incididunt ut labore et dolore magna aliqua. Ut enim ad minim veniam, quis nostrud exercitation ullamco laboris nisi ut aliquip ex ea commodo consequat.</p>
  <p class="abs" style="top:332px">Duis aute irure dolor in reprehenderit in voluptate velit esse cillum dolore eu fugiat nulla pariatur. Excepteur sint occaecat cupidatat non proident, sunt in culpa qui officia deserunt mollit anim id est laborum.</p>
  <a class="abs btn">Read More</a>
</section>

<!-- best sellers -->
<h2 class="abs title" style="top:2648px">BEST SELLERS</h2>
<svg class="abs arrow" style="left:37px;top:2918px" viewBox="0 0 40 24" fill="none" stroke="#555" stroke-width="2.2"><path d="M39 12H2M12 2L2 12l10 10"/></svg>
<svg class="abs arrow" style="left:1123px;top:2918px" viewBox="0 0 40 24" fill="none" stroke="#555" stroke-width="2.2"><path d="M1 12h37M28 2l10 10-10 10"/></svg>

<div class="abs prod" style="left:112px;top:2760px">
  <div class="abs add"><svg width="13" height="12" viewBox="0 0 18 16" fill="#f7b50c"><path d="M0 1h3l1 2h13l-2 7H5L3 2H0z"/><circle cx="6" cy="13.5" r="1.8"/><circle cx="14" cy="13.5" r="1.8"/></svg></div>
  <div class="abs photo" role="img" aria-label="Black hoodie" style="background:radial-gradient(circle,#2a2a2a 0%,#3a3a3a 50%,#f4f4f4 75%)"></div>
  <div class="abs stars">★★★★★</div>
  <h4 class="abs">Lorem ipsum dolor sit<br>amet consea</h4>
  <div class="abs price">$40.00</div>
</div>
<div class="abs prod" style="left:362px;top:2760px">
  <div class="abs add"><svg width="13" height="12" viewBox="0 0 18 16" fill="#f7b50c"><path d="M0 1h3l1 2h13l-2 7H5L3 2H0z"/><circle cx="6" cy="13.5" r="1.8"/><circle cx="14" cy="13.5" r="1.8"/></svg></div>
  <div class="abs photo" role="img" aria-label="Navy trucker cap" style="background:radial-gradient(ellipse,#1e2a44 0%,#2c3a5c 45%,#f4f4f4 75%)"></div>
  <div class="abs stars">★★★★★</div>
  <h4 class="abs">Lorem ipsum dolor sit<br>amet consea</h4>
  <div class="abs price">$65.00</div>
</div>
<div class="abs prod active" style="left:612px;top:2758px;width:226px;height:320px">
  <div class="abs add"><svg width="13" height="12" viewBox="0 0 18 16" fill="#0d2a78"><path d="M0 1h3l1 2h13l-2 7H5L3 2H0z"/><circle cx="6" cy="13.5" r="1.8"/><circle cx="14" cy="13.5" r="1.8"/></svg></div>
  <div class="abs photo" role="img" aria-label="Rolled blue yoga mat" style="background:radial-gradient(ellipse,#4c5fd6 0%,#5a6ce0 45%,#f4f4f4 75%)"></div>
  <div class="abs stars">★★★★★</div>
  <h4 class="abs">Lorem ipsum dolor sit<br>amet consea</h4>
  <div class="abs price">$40.00</div>
</div>
<a class="abs btn prod-btn" style="left:655px;top:3056px">Shop Now</a>
<div class="abs prod" style="left:863px;top:2760px">
  <div class="abs add"><svg width="13" height="12" viewBox="0 0 18 16" fill="#f7b50c"><path d="M0 1h3l1 2h13l-2 7H5L3 2H0z"/><circle cx="6" cy="13.5" r="1.8"/><circle cx="14" cy="13.5" r="1.8"/></svg></div>
  <div class="abs photo" role="img" aria-label="Silver diamond ring" style="background:radial-gradient(circle,#c9ccd2 0%,#e1e3e7 45%,#f6f6f6 75%)"></div>
  <div class="abs stars">★★★★★</div>
  <h4 class="abs">Lorem ipsum dolor sit<br>amet consea</h4>
  <div class="abs price">$65.00</div>
</div>

<!-- testimonials -->
<div class="abs band-ice" style="top:3216px;height:800px"></div>
<h2 class="abs title" style="top:3286px;font-weight:700">WHAT OUR <span style="color:var(--yellow)">CUSTOMERS</span> SAY</h2>
<div class="abs pager" style="left:42px;top:3559px;background:#d3dbe8"><svg width="10" height="14" viewBox="0 0 10 14" fill="none" stroke="#0d2a78" stroke-width="2.4"><path d="M8 1L2 7l6 6"/></svg></div>
<div class="abs pager" style="left:1122px;top:3559px;background:var(--navy)"><svg width="10" height="14" viewBox="0 0 10 14" fill="none" stroke="#fff" stroke-width="2.4"><path d="M2 1l6 6-6 6"/></svg></div>

<div class="abs quote" style="left:112px;top:3430px">
  <h5 class="abs">— MARCO T</h5><div class="abs stars">★★★★★</div>
  <p class="abs">Lorem ipsum dolor sit amet, conse ctetur adipiscing elit, sed do eiusmod tempor incididunt ut labore et dolore magna aliqua. Ut enim ad minim veniam, quis nostrud sedea.</p>
</div>
<div class="abs avatar" style="left:217px;top:3383px" role="img" aria-label="Customer portrait"></div>
<div class="abs quote" style="left:447px;top:3430px">
  <h5 class="abs">— PRIYA K</h5><div class="abs stars">★★★★★</div>
  <p class="abs">Lorem ipsum dolor sit amet, conse ctetur adipiscing elit, sed do eiusmod tempor incididunt ut labore et dolore magna aliqua. Ut enim ad minim veniam, quis nostrud sedea.</p>
</div>
<div class="abs avatar" style="left:552px;top:3383px" role="img" aria-label="Customer portrait"></div>
<div class="abs quote" style="left:783px;top:3430px">
  <h5 class="abs">— OWEN R</h5><div class="abs stars">★★★★★</div>
  <p class="abs">Lorem ipsum dolor sit amet, conse ctetur adipiscing elit, sed do eiusmod tempor incididunt ut labore et dolore magna aliqua. Ut enim ad minim veniam, quis nostrud sedea.</p>
</div>
<div class="abs avatar" style="left:888px;top:3383px" role="img" aria-label="Customer portrait"></div>

<!-- footer -->
<svg class="abs" style="left:0;top:3800px" width="1200" height="180" viewBox="0 0 1200 180">
  <path d="M0 170 C200 60 420 50 620 70 C820 90 1020 60 1200 20 L1200 180 L0 180Z" fill="#f7b50c"/>
  <path d="M0 180 C220 95 430 85 630 100 C830 115 1030 90 1200 55 L1200 180Z" fill="#0d2a78"/>
</svg>
<footer class="abs footer">
  <div class="abs brand">Kelvo-trabrand</div>
  <h6 class="abs" style="left:367px;top:50px">Navigation</h6>
  <ul class="abs links" style="left:367px;top:92px"><li>Home</li><li>Shop by Category</li><li>Deals</li><li>About Us</li></ul>
  <ul class="abs links" style="left:555px;top:92px"><li>Contact Us</li><li>Privacy Policy</li><li>Terms Of Conditions</li></ul>
  <h6 class="abs" style="left:823px;top:50px">Contact Us</h6>
  <div class="abs info" style="left:823px;top:92px"><span class="badge"><svg width="12" height="16" viewBox="0 0 12 16" fill="#f7b50c"><path d="M6 0a6 6 0 0 1 6 6c0 4-6 10-6 10S0 10 0 6a6 6 0 0 1 6-6z"/><circle cx="6" cy="6" r="2" fill="#fff"/></svg></span><span>465, Lorum Ipsum Dolore Sed,<br>United States</span></div>
  <div class="abs info" style="left:823px;top:152px"><span class="badge"><svg width="16" height="12" viewBox="0 0 16 12" fill="#f7b50c"><rect width="16" height="12" rx="1"/><path d="M0 1l8 6 8-6" stroke="#fff" fill="none" stroke-width="1.4"/></svg></span><span style="padding-top:7px">info@kelvo-trabrand.com</span></div>
  <div class="abs info" style="left:823px;top:208px"><span class="badge"><svg width="14" height="14" viewBox="0 0 16 16" fill="#f7b50c"><path d="M3 1l3 3-2 2c1 2 3 4 5 5l2-2 3 3-2 3C7 14 2 9 1 3z"/></svg></span><span style="padding-top:7px">+1 (555) 014 2290</span></div>
  <div class="abs rule"></div>
  <div class="abs cards"><span></span><span></span><span></span><span></span><span></span></div>
  <div class="abs copyright">2025 © All Rights Reserved - Kelvo-trabrand</div>
  <div class="abs social"><span class="on"></span><span></span><span></span><span></span></div>
</footer>

</body>
</html>
```